依頼詳細
現在当社で作成したチラシを元にしてフリーの挿絵や写真を利用して構成をしてください。イラレで作成したチラシデーターがダウンロードできます。
文章に関しては元がありますが言い回しなど変更していただいて結構です。
ロゴなどのデーターはそのまま使用をしてください。
サイズはB4でお願いします。
訪問看護と訪問介護の比率ですが、現在訪問介護が小さくなっていますが一緒にしていただいてかまいません。
記載項目
ロゴはかならず入れてください。訪問介護のロゴも募集しています。
希望イメージ
シンプル 複雑
単色 カラフル
暗い 明るい
日常 高級
遊び心 厳粛
未来的 伝統的
女性的 男性的
希望する色
緑系、黄・オレンジ系
納品ファイル
• 高解像度JPG (.jpg)
• イラストレーター形式 (.ai)
• フォトショップ形式 (.psd)
補足説明
となりに同グループの別会社があります。
内容等がほぼ同じなので当社とは別に採用させていただく可能性があります。
■ 選んだ理由

一番最初にご提案頂いたのですが、衝撃だったのがプロってここまですごいんだなという事でした。構成の仕方から文字の並べ方完璧です。
自分の中ではtoka-tokaさんが基準となっていたのですが、特にこれ良くない?って言ったわけではないですが10人のスタッフが全員toka-tokaさんを選択致しました。(びっくり)

■ 提案者全員のお礼・コメント

今回ご提案頂きましてありがとうございます。
次回の求人広告等で使用したい方もいたので個別にご連絡させて頂きます。
また、同じグループで求人を行っているところがあります。
今回ご提案頂いた案件に関して、JPgを保存しましたので各事業所に見てもらいますのでオファーがあった場合は買い取りさせていただきます。データーは保持してください。
当社でも別な施設オープンの際は改めてご連絡させて頂きます。
ありがとうございました。

```html
<!DOCTYPE html>
<html lang="ja">
<head>
<meta charset="utf-8">
<title>正看護師・PT・OT・ST 大募集</title>
<link href="https://fonts.googleapis.com/css2?family=Noto+Sans+JP:wght@400;700;900&display=swap" rel="stylesheet">
<style>
:root{
  --green:#2e9e3a;
  --green-dark:#1f7a2b;
  --green-pale:#e8f4cf;
  --yellow-pale:#fbf7d6;
  --red:#e3001b;
  --orange:#f08a00;
  --ink:#222;
  --white:#fff;
}
*{margin:0;padding:0;box-sizing:border-box}
html,body{width:844px;height:1200px;overflow:hidden;background:var(--white)}
body{font-family:"Noto Sans JP",sans-serif;color:var(--ink);position:relative}
.flyer{position:absolute;inset:0;background:linear-gradient(180deg,var(--white) 0,var(--green-pale) 45%,var(--yellow-pale) 60%,var(--white) 62%)}
.brand{position:absolute;left:14px;top:8px;display:flex;align-items:center;gap:8px;color:var(--green);font-weight:700;font-size:20px}
.brand-dot{width:22px;height:22px;border-radius:50%;background:var(--green)}
.hero-photo{position:absolute;left:0;top:46px;width:370px;height:330px;background:linear-gradient(160deg,#f4f8ee,#cfe3c2 60%,#9cc79a)}
.title{position:absolute;left:378px;top:52px;width:456px;text-align:center;font-weight:900;line-height:1;white-space:nowrap}
.title > div{text-shadow:0 0 4px #fff,3px 3px 0 #fff,-3px -3px 0 #fff,3px -3px 0 #fff,-3px 3px 0 #fff}
.title-nurse{font-size:100px;color:var(--red);letter-spacing:2px}
.title-therapy{margin-top:12px;font-size:72px;color:var(--green);letter-spacing:-1px}
.title-big{margin-top:6px;font-size:118px;color:var(--green);letter-spacing:10px}
.lead{position:absolute;left:20px;top:390px;width:340px;font-size:15px;font-weight:700;line-height:1.6;color:var(--green-dark)}
.session{position:absolute;left:380px;top:398px;width:450px}
.session-head{background:var(--green);color:var(--white);font-weight:900;font-size:24px;text-align:center;padding:3px 0;border-radius:4px}
.session p{font-size:13.5px;font-weight:700;line-height:1.5;margin-top:5px;color:var(--ink)}
.session .note{color:var(--red);font-size:13px;margin-top:2px}
.req-band{position:absolute;left:0;top:518px;width:844px;height:34px;background:var(--green);color:var(--white);font-weight:900;font-size:22px;padding-left:16px;line-height:34px}
.req-table{position:absolute;left:14px;top:560px;width:636px;font-size:13px;line-height:1.55;border-collapse:collapse}
.req-table th{width:62px;vertical-align:top;text-align:left;color:var(--green-dark);font-weight:900;padding:3px 0}
.req-table td{padding:3px 0;border-bottom:1px dashed #9cc79a}
.req-table em{font-style:normal;color:var(--red);font-weight:900;font-size:16px}
.novice{position:absolute;left:660px;top:558px;width:172px;height:204px;border:2px solid var(--orange);border-radius:8px;background:var(--white);padding:8px;font-size:12px;line-height:1.5}
.novice h3{background:var(--orange);color:var(--white);font-size:16px;text-align:center;border-radius:4px;margin-bottom:6px}
.philosophy{position:absolute;left:14px;top:774px;width:482px;height:144px;background:var(--white);border:2px solid var(--green);border-radius:8px;padding:30px 12px 8px;font-size:13px;line-height:1.6}
.philosophy h3{position:absolute;left:50%;top:-14px;transform:translateX(-50%);background:var(--orange);color:var(--white);font-size:16px;padding:2px 20px;border-radius:14px;white-space:nowrap}
.newsite{position:absolute;left:506px;top:774px;width:326px;height:144px;background:var(--white);border:2px solid var(--green);border-radius:8px;padding:8px 12px;font-size:13px;line-height:1.6}
.newsite h3{color:var(--green);font-size:19px;font-weight:900;text-align:center;margin-bottom:4px}
.also{position:absolute;left:0;top:930px;width:844px;height:184px;background:var(--green-pale)}
.also-label{position:absolute;left:0;top:0;width:180px;height:184px;background:var(--green);color:var(--white);font-weight:900;font-size:62px;line-height:1.05;display:flex;flex-direction:column;align-items:center;justify-content:center}
.jobs{position:absolute;left:190px;top:8px;display:flex;gap:8px}
.job{width:210px;height:168px;background:var(--white);border:2px solid var(--orange);border-radius:8px;padding:6px 10px;font-size:12px;line-height:1.45}
.job h4{background:var(--orange);color:var(--white);text-align:center;font-size:17px;border-radius:4px;margin-bottom:6px}
.job .pay{color:var(--red);font-weight:900;font-size:24px}
.contact{position:absolute;left:0;top:1114px;width:844px;height:86px;background:var(--green);color:var(--white);display:flex;align-items:center;padding:0 16px;gap:14px}
.contact-label{font-weight:900;font-size:22px}
.contact-tel{display:flex;align-items:center;gap:8px;font-weight:900;font-size:44px;letter-spacing:1px}
.contact-tel svg{width:40px;height:40px}
.contact-who{font-size:14px;font-weight:700;line-height:1.5}
</style>
</head>
<body>
<div class="flyer">
  <div class="brand"><span class="brand-dot"></span>ケアリーフ港南訪問看護リハビリステーション</div>

  <div class="hero-photo" role="img" aria-label="白衣姿で微笑む看護師の写真"></div>

  <h1 class="title">
    <div class="title-nurse">正看護師</div>
    <div class="title-therapy">PT・OT・ST</div>
    <div class="title-big">大募集</div>
  </h1>

  <p class="lead">病棟勤務とは違う本当の意味での<br>「看護」、「人」とつながる看護を<br>目指してみませんか。</p>

  <section class="session">
    <div class="session-head">事前説明会随時開催!!</div>
    <p>話だけでも聞いてみたい(履歴書不要)という方も歓迎します。<br>お手軽にお電話でご予約のうえ、ご来社ください。</p>
    <p class="note">※日時はご相談ください。</p>
  </section>

  <div class="req-band">■募集要項　■正看護士/PT・OT・ST</div>

  <table class="req-table">
    <tr><th>【給与】</th><td>正社員：月給<em>28万円</em>〜（訪問単価4,000円/件）月給<em>36万円</em>〜<br>パート：訪問単価<em>4,000円</em>/件　同行研修期間中は時給1,500円</td></tr>
    <tr><th>【資格】</th><td>各種職種に応じた資格をお持ちの方</td></tr>
    <tr><th>【時間】</th><td>正社員 9:00〜18:00　パート 日数・時間はご相談ください</td></tr>
    <tr><th>【休日】</th><td>土・日・祝日、年末年始（オンコール対応可能な方優遇）</td></tr>
    <tr><th>【待遇】</th><td>各種社会保険完備、賞与年2回、交通費規定支給<br>車・バイク通勤可、研修制度あり</td></tr>
  </table>

  <aside class="novice">
    <h3>未経験でも安心</h3>
    <p>訪問看護がはじめての方も、先輩スタッフが同行し丁寧に指導します。ブランクのある方も歓迎。研修と相談体制で一人ひとりを支えます。</p>
  </aside>

  <section class="philosophy">
    <h3>当社の基本理念</h3>
    <p>ご利用者様とご家族が、住み慣れたご自宅で安心して暮らせるよう、心のこもった看護とリハビリを届けます。スタッフ一人ひとりが成長し、地域に信頼される事業所を目指しています。</p>
  </section>

  <section class="newsite">
    <h3>新たに事業所をOPENします</h3>
    <p>地域のニーズに応えるため、新事業所を開設します。立ち上げメンバーとして一緒に働ける仲間を募集しています。</p>
  </section>

  <section class="also">
    <div class="also-label"><span>同時</span><span>募集</span></div>
    <div class="jobs">
      <div class="job"><h4>介護職員</h4><p>正社員：月給</p><p class="pay">24万円〜</p><p>介護福祉士・初任者研修修了の方</p></div>
      <div class="job"><h4>登録ヘルパー</h4><p>身体介護：時給</p><p class="pay">2,000円〜</p><p>生活援助：時給1,600円〜</p></div>
      <div class="job"><h4>常勤ヘルパー</h4><p>介護福祉士：時給</p><p class="pay">1,200円〜</p><p>初任者研修：時給1,100円〜</p></div>
    </div>
  </section>

  <footer class="contact">
    <span class="contact-label">応募専用ダイヤル</span>
    <span class="contact-tel">
      <svg viewBox="0 0 24 24" aria-hidden="true"><circle cx="12" cy="12" r="12" fill="#fff"/><path d="M8 6l2 3-1.3 1.3a8 8 0 0 0 5 5L15 14l3 2-1 2.5c-5 0-10-5-10-10z" fill="#2e9e3a"/></svg>
      045-610-3827
    </span>
    <span class="contact-who">採用担当/田中<br>(有)ミドリケア</span>
  </footer>
</div>
</body>
</html>
```